Design for Certificate for Educational Program

Dear Designer,
We need a design for a certificate once participants graduate from our educational program. You find our website here (pls take the logo from the page):
https://www.quillmetric.com/
The briefing for the design should fulfill the following requirements / entail the following elements:
- Name of participant
- Name of program:
QuillMetric developer
or
QuillMetric architect
- there needs to be a a place on the certificate where a cool hologram would go
- Logo
Research what else should go there / what would be on a certificate.
Style:
- futuristic
- bold
- The program is for software developers - think about what things in this industry look like, what might fit to this target group
- cool
- NOT like a Bachelor program
- colors: blues and greens, maybe some black / grey
- professional
- authority
Our company presentations use Nunito as font. But you can use any font you want as long as it fulfills above requirements.
Timeline is: first delivery by Friday, Dec. 16, 06:00pm ET (Orlando), the latest.
For questions, pls feel free to approach me.
All the best,
Dr. Anselm Brodtke
Software programmers

```html
<!DOCTYPE html>
<html lang="en">
<head>
<meta charset="utf-8">
<title>QuillMetric Certificate</title>
<link href="https://fonts.googleapis.com/css2?family=Montserrat:wght@400;500;600;700;800&family=Great+Vibes&display=swap" rel="stylesheet">
<style>
  :root {
    --page-bg: #f3f4f6;
    --sheet-bg: #eef6fc;
    --ink: #1b2230;
    --accent: #3b8ed8;
    --accent-light: #8ec3ee;
    --accent-pale: #cfe5f7;
    --body-text: #3a4250;
    --gold: #d3a43c;
    --gold-light: #f1d486;
  }
  * { margin: 0; padding: 0; box-sizing: border-box; }
  html, body { width: 773px; height: 1200px; overflow: hidden; }
  body {
    background: var(--page-bg);
    font-family: "Montserrat", sans-serif;
    position: relative;
  }
  .certificate {
    position: absolute;
    left: 20px;
    top: 340px;
    width: 733px;
    height: 520px;
    background: var(--sheet-bg);
    overflow: hidden;
    box-shadow: 0 2px 10px rgba(0,0,0,0.08);
  }
  .certificate__shapes { position: absolute; inset: 0; }
  .certificate__content {
    position: absolute;
    inset: 0;
    text-align: center;
  }
  .title {
    position: absolute; top: 62px; width: 100%;
    font-size: 44px; font-weight: 500; letter-spacing: 5px; color: var(--ink);
  }
  .subtitle {
    position: absolute; top: 118px; width: 100%;
    font-size: 17px; font-weight: 500; letter-spacing: 3px; color: var(--accent);
  }
  .presented {
    position: absolute; top: 182px; width: 100%;
    font-size: 8px; font-weight: 600; letter-spacing: 1.5px; color: var(--ink);
  }
  .recipient {
    position: absolute; top: 198px; width: 100%;
    font-family: "Great Vibes", cursive; font-size: 64px; color: var(--ink);
    line-height: 1;
  }
  .recipient-line {
    position: absolute; top: 272px; left: 226px; width: 281px; height: 1px;
    background: var(--ink);
  }
  .award-name {
    position: absolute; top: 290px; width: 100%;
    font-size: 14px; font-weight: 700; letter-spacing: 1px; color: var(--accent);
  }
  .description {
    position: absolute; top: 316px; left: 210px; width: 313px;
    font-size: 7.5px; line-height: 1.45; color: var(--body-text);
  }
  .award-seal { position: absolute; left: 228px; top: 382px; width: 64px; height: 64px; }
  .brand {
    position: absolute; left: 400px; top: 392px; width: 130px; text-align: center;
  }
  .brand__name { font-size: 21px; font-weight: 800; color: var(--accent); line-height: 1; }
  .brand__program {
    font-size: 11px; font-weight: 600; letter-spacing: 1px; color: var(--ink); margin-top: 5px;
  }
</style>
</head>
<body>
  <main class="certificate">
    <svg class="certificate__shapes" viewBox="0 0 733 520" width="733" height="520" aria-hidden="true">
      <defs>
        <linearGradient id="band" x1="0" y1="0" x2="1" y2="1">
          <stop offset="0" stop-color="#4e9fe0"/>
          <stop offset="1" stop-color="#bcdcf5"/>
        </linearGradient>
        <linearGradient id="bandSoft" x1="0" y1="0" x2="1" y2="0">
          <stop offset="0" stop-color="#cfe5f7"/>
          <stop offset="1" stop-color="#eaf4fc"/>
        </linearGradient>
      </defs>
      <!-- left geometry -->
      <polygon points="0,0 36,0 36,460 0,520" fill="url(#band)"/>
      <polygon points="36,0 100,0 60,70 36,70" fill="url(#bandSoft)"/>
      <polygon points="36,90 70,130 70,380 36,430" fill="#a9d2f3"/>
      <polygon points="70,130 110,175 110,320 70,380" fill="url(#bandSoft)"/>
      <polygon points="0,470 60,420 140,520 0,520" fill="#6fb3ea"/>
      <!-- right geometry -->
      <polygon points="733,0 640,0 700,90 733,90" fill="url(#band)"/>
      <polygon points="733,90 700,90 700,240 733,270" fill="#a9d2f3"/>
      <polygon points="700,90 660,140 660,220 700,240" fill="url(#bandSoft)"/>
      <polygon points="733,330 690,380 733,430" fill="#6fb3ea"/>
      <polygon points="733,430 640,520 733,520" fill="url(#band)"/>
      <g stroke="#8ec3ee" stroke-width="1.2">
        <line x1="630" y1="330" x2="630" y2="500"/>
        <line x1="640" y1="330" x2="640" y2="500"/>
        <line x1="650" y1="330" x2="650" y2="500"/>
        <line x1="660" y1="330" x2="660" y2="500"/>
        <line x1="670" y1="330" x2="670" y2="500"/>
        <line x1="680" y1="330" x2="680" y2="480"/>
      </g>
    </svg>

    <section class="certificate__content">
      <h1 class="title">CERTIFICATE</h1>
      <p class="subtitle">OF APPRECIATION</p>
      <p class="presented">THIS CERTIFICATE IS PRESENTED TO</p>
      <p class="recipient">Maren holt</p>
      <div class="recipient-line"></div>
      <h2 class="award-name">EDUCATIONAL PROGRAM AWARD</h2>
      <p class="description">Lorem Ipsum is simply dummy text of the printing and typesetting industry. Lorem Ipsum has been the industry's standard dummy text ever since the 1500s, when an unknown printer took a galley of type and scrambled it to make a type specimen book.</p>

      <svg class="award-seal" viewBox="0 0 64 64" role="img" aria-label="Award seal">
        <circle cx="32" cy="32" r="26" fill="var(--gold)"/>
        <circle cx="32" cy="32" r="20" fill="var(--gold-light)"/>
      </svg>

      <div class="brand">
        <p class="brand__name">QuillMetric</p>
        <p class="brand__program">DEVELOPER</p>
      </div>
    </section>
  </main>
</body>
</html>
```